Fieldstone Sporting
F.S.S. Sports
Project: Fieldstone Sporting
Fieldstone Sporting - Sports
Creative Brief
Use same font as used in my logo
Use your better judgement
Professional
Weston L. Barrow Jr.
CEO
Ashford Glen, MD
W.barrow17@quillmail.example
www.FSSsports.example
Logo and web address
Concepts
Business card and stationary design. We provide umpires & referees for teams/organizations.

```html
<!DOCTYPE html>
<html lang="en">
<head>
<meta charset="utf-8">
<title>Fieldstone Sporting – Stationery</title>
<link rel="stylesheet" href="https://fonts.googleapis.com/css2?family=Open+Sans:wght@400;700;800&display=swap">
<style>
  :root {
    --navy: #2f3d8f;
    --green: #7cc242;
    --ink: #4a4a4a;
    --paper: #ffffff;
    --stage: #ffffff;
    --frame: #d9d9d9;
    --shadow: rgba(0,0,0,0.28);
    --runner-a: #c9d3e6;
    --runner-b: #8e9cbc;
  }
  * { box-sizing: border-box; margin: 0; padding: 0; }
  html, body { width: 1200px; height: 681px; overflow: hidden; background: var(--stage); }
  body { font-family: "Open Sans", Arial, sans-serif; color: var(--ink); position: relative; }

  .presentation-frame {
    position: absolute; left: 12px; top: 12px; width: 1176px; height: 641px;
    border: 1px solid var(--frame);
  }
  .piece {
    position: absolute; background: var(--paper); overflow: hidden;
    box-shadow: 3px 5px 10px var(--shadow);
  }
  .swoosh { position: absolute; inset: 0; width: 100%; height: 100%; }

  .wordmark {
    position: absolute; display: flex; align-items: center; gap: 5px;
    font-weight: 800; color: var(--navy); white-space: nowrap; line-height: 1;
  }
  .wordmark .mark-dot { border-radius: 50%; background: var(--green); flex: none; }

  .contact-line { position: absolute; font-size: 7px; color: var(--ink); white-space: nowrap; }

  /* Envelope front */
  .envelope-front { left: 60px; top: 101px; width: 473px; height: 211px; }
  .envelope-front .wordmark { left: 58px; top: 28px; font-size: 16px; }
  .envelope-front .mark-dot { width: 11px; height: 11px; }
  .envelope-front .contact-line { left: 58px; top: 78px; }

  /* Envelope back */
  .envelope-back { left: 60px; top: 365px; width: 473px; height: 199px; }
  .envelope-back .flap { position: absolute; inset: 0; width: 100%; height: 100%; }
  .envelope-back .runner-art {
    position: absolute; left: 206px; top: 42px; width: 60px; height: 36px;
    background: linear-gradient(90deg, var(--runner-b), var(--runner-a));
    border-radius: 4px;
  }

  /* Letterhead */
  .letterhead { left: 619px; top: 43px; width: 317px; height: 581px; }
  .letterhead .wordmark { left: 72px; top: 32px; font-size: 18px; }
  .letterhead .mark-dot { width: 12px; height: 12px; }
  .letterhead .contact-line { left: 72px; font-size: 6.5px; }
  .letterhead .line-1 { top: 80px; }
  .letterhead .line-2 { top: 90px; }
  .letterhead .runner-watermark {
    position: absolute; left: 150px; top: 395px; width: 150px; height: 140px;
    background: radial-gradient(ellipse at center, rgba(180,186,196,0.35), rgba(255,255,255,0) 70%);
  }

  /* Business cards */
  .card-front { left: 967px; top: 144px; width: 161px; height: 103px; }
  .card-front .wordmark { left: 60px; top: 10px; font-size: 8px; gap: 3px; }
  .card-front .mark-dot { width: 6px; height: 6px; }
  .card-front .holder-name { position: absolute; left: 22px; top: 30px; font-size: 6px; font-weight: 700; color: var(--navy); }
  .card-front .holder-title { position: absolute; left: 22px; top: 38px; font-size: 5px; }
  .card-front .card-details { position: absolute; left: 22px; top: 54px; font-size: 4.2px; line-height: 1.45; }
  .card-front .runner-art {
    position: absolute; left: 104px; top: 28px; width: 50px; height: 34px;
    background: linear-gradient(90deg, var(--runner-b), var(--navy));
    border-radius: 4px;
  }

  .card-back { left: 967px; top: 271px; width: 161px; height: 106px; }
  .card-back .wordmark { left: 50%; top: 40px; transform: translateX(-50%); font-size: 9px; gap: 3px; }
  .card-back .mark-dot { width: 7px; height: 7px; }
  .card-back .web { position: absolute; left: 0; right: 0; top: 62px; text-align: center; font-size: 4.5px; }
</style>
</head>
<body>
  <div class="presentation-frame"></div>

  <section class="piece envelope-front" aria-label="Envelope front">
    <svg class="swoosh" viewBox="0 0 473 211" preserveAspectRatio="none" aria-hidden="true">
      <path d="M52 0 C30 70 24 140 30 211 L22 211 C14 140 22 70 42 0 Z" fill="var(--green)"/>
      <path d="M34 0 C14 70 10 150 24 211 L12 211 C-2 150 2 70 22 0 Z" fill="var(--navy)"/>
    </svg>
    <div class="wordmark"><span class="mark-dot"></span>Fieldstone Sporting</div>
    <p class="contact-line">Ashford Glen, MD &nbsp;|&nbsp; www.FSSsports.example</p>
  </section>

  <section class="piece envelope-back" aria-label="Envelope back">
    <svg class="flap" viewBox="0 0 473 199" preserveAspectRatio="none" aria-hidden="true">
      <path d="M0 6 L20 6 L236 62 L453 6 L473 6" fill="none" stroke="#b5b5b5" stroke-width="1"/>
    </svg>
    <div class="runner-art" role="img" aria-label="Illustration of sprinting athletes"></div>
  </section>

  <section class="piece letterhead" aria-label="Letterhead">
    <svg class="swoosh" viewBox="0 0 317 581" preserveAspectRatio="none" aria-hidden="true">
      <path d="M62 0 C28 160 22 380 38 581 L28 581 C12 380 18 160 52 0 Z" fill="var(--green)"/>
      <path d="M34 0 C10 180 8 400 26 581 L12 581 C-6 400 -2 180 22 0 Z" fill="var(--navy)"/>
    </svg>
    <div class="wordmark"><span class="mark-dot"></span>Fieldstone Sporting</div>
    <p class="contact-line line-1">Ashford Glen, MD &nbsp;|&nbsp; Phone: 410 555 0182</p>
    <p class="contact-line line-2">Email: W.barrow17@quillmail.example &nbsp;|&nbsp; www.FSSsports.example</p>
    <div class="runner-watermark" role="img" aria-label="Faint illustration of sprinting athletes"></div>
  </section>

  <section class="piece card-front" aria-label="Business card front">
    <svg class="swoosh" viewBox="0 0 161 103" preserveAspectRatio="none" aria-hidden="true">
      <path d="M16 0 C8 35 8 70 12 103 L8 103 C4 70 4 35 12 0 Z" fill="var(--green)"/>
      <path d="M9 0 C2 35 2 70 6 103 L0 103 L0 0 Z" fill="var(--navy)"/>
    </svg>
    <div class="wordmark"><span class="mark-dot"></span>Fieldstone Sporting</div>
    <p class="holder-name">Weston L. Barrow Jr.</p>
    <p class="holder-title">CEO</p>
    <p class="card-details">Ashford Glen, MD<br>410 555 0182<br>W.barrow17@quillmail.example<br>www.FSSsports.example</p>
    <div class="runner-art" role="img" aria-label="Illustration of sprinting athletes"></div>
  </section>

  <section class="piece card-back" aria-label="Business card back">
    <div class="wordmark"><span class="mark-dot"></span>Fieldstone Sporting</div>
    <p class="web">www.FSSsports.example</p>
  </section>
</body>
</html>
```